Lira Vantell Music Flyer for Social Media

The flyer needs to include the networks Lira Vantell music is distributed on such as TuneHarbor, WaveCastFM, Brook, and Soundly. This flyer will be posted on social media websites such as friendloop, Pictogrove, and Chirpnet. The flyer will also be listed on the music artist official website. The artist logo is attached for additional creative ideas.

Target Market(s)

Music lovers

Industry/Entity Type

Music Download

Requirements
Must have
• Must have the music networks listed on the photo and the artist name.
Nice to have
• It would be nice to have the website listed: www.liravantell.example and artist logo.
Should not have
• Anything that is not listed in the project description.

```html
<!DOCTYPE html>
<html lang="en">
<head>
<meta charset="utf-8">
<title>Lira Vantell – Music Flyer</title>
<link rel="stylesheet" href="https://fonts.googleapis.com/css2?family=Cormorant+Garamond:wght@400;500&family=Montserrat:wght@400;600&display=swap">
<style>
  :root {
    --ink: #ffffff;
    --hair-dark: #1e1418;
    --hair-mid: #3b2630;
    --skin-light: #a0625a;
    --skin: #6e3f3b;
    --lips: #c2607a;
    --violet: #a667b8;
    --lilac: #d9a6ea;
    --shirt: #e4b8ee;
    --frame: rgba(255, 255, 255, 0.92);
  }
  * { margin: 0; padding: 0; box-sizing: border-box; }
  html, body { width: 1200px; height: 1200px; overflow: hidden; background: var(--hair-dark); }
  .flyer { position: relative; width: 1200px; height: 1200px; overflow: hidden; color: var(--ink); }

  .artist-photo {
    position: absolute; inset: 0;
    background:
      radial-gradient(ellipse 250px 330px at 250px 430px, var(--skin-light) 0%, var(--skin) 55%, rgba(110,63,59,0) 100%),
      radial-gradient(ellipse 420px 520px at 240px 430px, rgba(70,40,44,0.9) 0%, rgba(70,40,44,0) 100%),
      radial-gradient(ellipse 520px 260px at 300px 1120px, var(--shirt) 0%, rgba(228,184,238,0.6) 50%, rgba(228,184,238,0) 100%),
      linear-gradient(180deg, rgba(30,20,24,0) 0%, rgba(30,20,24,0) 55%, rgba(166,103,184,0.7) 85%, var(--lilac) 100%),
      linear-gradient(90deg, var(--hair-mid) 0%, var(--hair-dark) 45%, #2a1b22 75%, var(--hair-mid) 100%);
  }

  .frame { position: absolute; inset: 0; }

  .brand-name {
    position: absolute; top: 218px; left: 792px; transform: translateX(-50%);
    font-family: "Cormorant Garamond", serif; font-weight: 500; font-size: 58px;
    white-space: nowrap; line-height: 1;
  }
  .brand-caps {
    position: absolute; top: 332px; left: 794px; transform: translateX(-50%);
    font-family: "Cormorant Garamond", serif; font-weight: 400; font-size: 24px;
    letter-spacing: 0.42em; text-transform: uppercase; white-space: nowrap; line-height: 1;
  }

  .network {
    position: absolute; transform: translate(-50%, -50%);
    display: flex; align-items: center; gap: 12px;
    font-family: "Montserrat", sans-serif; font-weight: 600; font-size: 32px;
    white-space: nowrap; line-height: 1;
  }
  .network--tuneharbor { left: 650px; top: 556px; }
  .network--brook      { left: 924px; top: 556px; }
  .network--soundly    { left: 650px; top: 686px; }
  .network--wavecast   { left: 924px; top: 686px; }
  .network-dot { width: 28px; height: 28px; border-radius: 50%; background: var(--ink); flex: none; }

  .website {
    position: absolute; top: 876px; left: 802px; transform: translateX(-50%);
    font-family: "Montserrat", sans-serif; font-weight: 400; font-size: 24px;
    letter-spacing: 0.16em; white-space: nowrap; line-height: 1;
  }
</style>
</head>
<body>
<main class="flyer">
  <div class="artist-photo" role="img" aria-label="Portrait of the smiling artist with voluminous curly hair and a striped top, washed in purple light"></div>

  <svg class="frame" width="1200" height="1200" viewBox="0 0 1200 1200" aria-hidden="true">
    <g stroke="var(--frame)" stroke-width="2" fill="none">
      <line x1="451" y1="336" x2="618" y2="336"/>
      <line x1="968" y1="336" x2="1133" y2="336"/>
      <line x1="451" y1="336" x2="451" y2="889"/>
      <line x1="1133" y1="336" x2="1133" y2="889"/>
      <line x1="451" y1="889" x2="580" y2="889"/>
      <line x1="1024" y1="889" x2="1133" y2="889"/>
    </g>
  </svg>

  <div class="brand-name">Lira Vantell</div>
  <div class="brand-caps">Lira Vantell</div>

  <section class="networks" aria-label="Listen on">
    <div class="network network--tuneharbor"><span class="network-dot"></span>TuneHarbor</div>
    <div class="network network--brook"><span class="network-dot"></span>Brook</div>
    <div class="network network--soundly"><span class="network-dot"></span>Soundly</div>
    <div class="network network--wavecast"><span class="network-dot"></span>WaveCastFM</div>
  </section>

  <div class="website">www.liravantell.example</div>
</main>
</body>
</html>
```